Personal creative Biz Card Design

Need personal yet natural and organic design. The cards I have now are well designed but look too commercial. I want more organic FEELING kind of card. I thought having a headshot would make it more personal... but maybe a sketch effect (or line drawing effect) of face better (?). Maybe in a gray or tungsten color?

Target Market(s)

Well, everyone i give card to will have already seen me face-to-face so that is one thing. Mostly yoga students and people interested in improving their fitness or general health. People looking for wellness, a personal fitness trainer, a yoga teacher

Industry/Entity Type

Health And Wellness

Contact Information for Business Card

I provided examples

Requirements
Must have
• My main logo
• My name

```html
<!DOCTYPE html>
<html lang="en">
<head>
<meta charset="utf-8">
<title>Theo Marlow – Business Card</title>
<link href="https://fonts.googleapis.com/css2?family=Questrial&family=Montserrat:wght@700&display=swap" rel="stylesheet">
<style>
  :root {
    --backdrop: #2b2b2b;
    --card: #ffffff;
    --green: #4b9a2e;
    --ink: #2f2f2f;
    --ink-soft: #555555;
  }
  * { box-sizing: border-box; margin: 0; padding: 0; }
  html, body {
    width: 1200px;
    height: 1006px;
    overflow: hidden;
    background: var(--backdrop);
  }
  body {
    display: flex;
    flex-direction: column;
    align-items: center;
    justify-content: center;
    gap: 60px;
    font-family: "Questrial", sans-serif;
    color: var(--ink);
  }
  .card {
    width: 700px;
    height: 400px;
    background: var(--card);
    border-radius: 3px;
    box-shadow: 0 8px 24px rgba(0,0,0,.35);
    position: relative;
  }

  /* Front */
  .card--front {
    display: flex;
    align-items: center;
    justify-content: center;
  }
  .brand {
    display: flex;
    align-items: center;
    gap: 16px;
  }
  .brand__dot {
    width: 26px;
    height: 26px;
    border-radius: 50%;
    background: var(--green);
  }
  .brand__name {
    font-family: "Questrial", sans-serif;
    font-size: 44px;
    letter-spacing: 1px;
    color: var(--green);
  }

  /* Back */
  .card--back {
    display: flex;
    align-items: center;
    padding: 0 60px 0 50px;
  }
  .card--back .brand {
    width: 280px;
    justify-content: center;
    gap: 12px;
  }
  .card--back .brand__dot { width: 20px; height: 20px; }
  .card--back .brand__name { font-size: 28px; }

  .details {
    border-left: 2px solid var(--green);
    padding: 10px 0 10px 24px;
    height: 270px;
    display: flex;
    flex-direction: column;
    justify-content: space-between;
  }
  .details__name {
    font-family: "Montserrat", sans-serif;
    font-weight: 700;
    font-size: 22px;
    color: var(--green);
    line-height: 1.1;
  }
  .details__title {
    font-size: 18px;
    line-height: 1.3;
  }
  .details__address {
    font-size: 19px;
    line-height: 1.35;
  }
  .contact-list {
    list-style: none;
    font-size: 19px;
    line-height: 1.4;
  }
  .contact-list li {
    display: flex;
    align-items: center;
    gap: 12px;
  }
  .contact-list svg {
    width: 16px;
    height: 16px;
    flex: none;
    fill: var(--green);
  }
</style>
</head>
<body>

  <section class="card card--front" aria-label="Card front">
    <div class="brand">
      <span class="brand__dot"></span>
      <span class="brand__name">THEO MARLOW</span>
    </div>
  </section>

  <section class="card card--back" aria-label="Card back">
    <div class="brand">
      <span class="brand__dot"></span>
      <span class="brand__name">THEO MARLOW</span>
    </div>

    <div class="details">
      <div>
        <p class="details__name">Your Name</p>
        <p class="details__title">Job Title</p>
      </div>
      <p class="details__address">PO Box No. 123, Street Name<br>City Name, Country 4567</p>
      <ul class="contact-list">
        <li>
          <svg viewBox="0 0 16 16" aria-hidden="true"><path d="M2 5c0-2 2-3 6-3s6 1 6 3v1h-3V5H5v1H2zM4 7h8l2 6H2zm4 1.5a2 2 0 1 0 0 4 2 2 0 0 0 0-4z"/></svg>
          (123) 456 7890
        </li>
        <li>
          <svg viewBox="0 0 16 16" aria-hidden="true"><path d="M4.5 1h7a1 1 0 0 1 1 1v12a1 1 0 0 1-1 1h-7a1 1 0 0 1-1-1V2a1 1 0 0 1 1-1zm.5 2v9h6V3zm3 10a.8.8 0 1 0 0 1.6.8.8 0 0 0 0-1.6z"/></svg>
          (123) 456 7890
        </li>
        <li>
          <svg viewBox="0 0 16 16" aria-hidden="true"><path d="M1 3h14v10H1zm1.5 1.2v.3L8 8.5l5.5-4V4.2zm0 2.1V12h11V6.3L8 10.3z"/></svg>
          info@theomarlow.com
        </li>
        <li>
          <svg viewBox="0 0 16 16" aria-hidden="true"><path d="M8 1a7 7 0 1 0 0 14A7 7 0 0 0 8 1zm0 1.3c.9 0 1.8 1.6 2.1 3.9H5.9C6.2 3.9 7.1 2.3 8 2.3zM2.4 7.3h2.3c0 .5 0 1 .1 1.4H2.4zm3.5 0h4.2a10 10 0 0 1 0 1.4H5.9a10 10 0 0 1 0-1.4zm5.4 0h2.3v1.4h-2.4zM5.9 9.8h4.2c-.3 2.3-1.2 3.9-2.1 3.9s-1.8-1.6-2.1-3.9z"/></svg>
          www.theomarlow.com
        </li>
      </ul>
    </div>
  </section>

</body>
</html>
```